velto GmbH - Business Cards etc.
velto GmbH
Project: velto GmbH - Business Cards etc.
velto GmbH - Business Cards etc. - Retailers
Creative Brief
Professional
Konrad Wieslauer
CEO
Gisela Brandtner Str. 23 76139 Karlsruhe
k.wieslauer@veltohouse.com
www.veltohouse.com
The business card MUST have the following format: 85 x 55mm PLUS a 3mm addition on every side. This means the image size must be 91 x 61mm
Concepts
Business Cards/Letterhead/ Envelopes/Notepads/Tshirt/labels for tiny tall crate
Business cards and company letter head for Osaka Dine Court
konrad konrad
I don't have a logo unfortunately. I've started a logo design project but it was not successful. I really need biz cards now and want to find a logo later. The logo on the biz cards is not so important in this case.
I wonder why there are so few contributions to this project? What's missing? How can I help?

```html
<!DOCTYPE html>
<html lang="de">
<head>
<meta charset="utf-8">
<title>velto GmbH – Visitenkarte Konrad Wieslauer</title>
<link rel="stylesheet" href="https://fonts.googleapis.com/css2?family=Tinos&family=Roboto+Condensed:wght@400&display=swap">
<style>
  :root {
    --paper: #ffffff;
    --page: #ffffff;
    --edge: #bdbdbd;
    --brand-orange: #f5821f;
    --ink: #1a1a1a;
    --reverse: #ffffff;
  }
  html, body {
    margin: 0;
    padding: 0;
    width: 1200px;
    height: 871px;
    overflow: hidden;
    background: var(--page);
  }
  .canvas {
    position: relative;
    width: 1200px;
    height: 871px;
  }
  .business-card {
    position: absolute;
    left: 158px;
    top: 144px;
    width: 891px;
    height: 576px;
    background: var(--paper);
    box-sizing: border-box;
    border: 2px solid var(--edge);
    overflow: hidden;
  }
  .corner-accent {
    position: absolute;
    right: 0;
    top: 0;
    width: 82px;
    height: 53px;
    background: var(--brand-orange);
  }
  .holder {
    position: absolute;
    left: 34px;
    top: 44px;
    margin: 0;
    font-family: "Tinos", "Times New Roman", serif;
    color: var(--ink);
  }
  .holder-name {
    margin: 0;
    font-weight: 400;
    font-size: 64px;
    line-height: 1;
    letter-spacing: 0.5px;
  }
  .holder-role {
    margin: 10px 0 0 2px;
    font-weight: 400;
    font-size: 28px;
    line-height: 1;
  }
  .brand-block {
    position: absolute;
    left: 0;
    bottom: 0;
    width: 382px;
    height: 209px;
    background: var(--brand-orange);
  }
  .brand-name {
    position: absolute;
    left: 40px;
    top: 66px;
    margin: 0;
    font-family: "Roboto Condensed", "Arial Narrow", sans-serif;
    font-weight: 400;
    font-size: 60px;
    line-height: 1;
    color: var(--reverse);
    white-space: nowrap;
  }
  .contact-details {
    position: absolute;
    left: 389px;
    top: 356px;
    margin: 0;
    font-family: "Roboto Condensed", "Arial Narrow", sans-serif;
    font-style: normal;
    font-size: 26px;
    line-height: 29px;
    color: var(--ink);
  }
  .contact-details span {
    display: block;
    white-space: nowrap;
  }
</style>
</head>
<body>
  <main class="canvas">
    <section class="business-card" aria-label="Visitenkarte">
      <div class="corner-accent"></div>
      <header class="holder">
        <h1 class="holder-name">Konrad Wieslauer</h1>
        <p class="holder-role">CEO</p>
      </header>
      <div class="brand-block">
        <p class="brand-name">velto GmbH</p>
      </div>
      <address class="contact-details">
        <span>Gisela Brandtner Str. 23</span>
        <span>76139 Karlsruhe</span>
        <span>Phone +49 (0) 721 384 6190</span>
        <span>Fax +49 (0) 721 384 6191</span>
        <span>Email: k.wieslauer@veltohouse.com</span>
        <span>www.veltohouse.com</span>
      </address>
    </section>
  </main>
</body>
</html>
```